New Business Cards / Logo update

Logo:
can be updated but wanted pricing

New Business Cards:
take our existing business cards and upgrade them from a design perspective. We have two versions
Inside sales team does not have a cell phone and they use an appointment back slot.
Outside project managers and leadership uses a slogan backing and will have cell phones.

```html
<!DOCTYPE html>
<html lang="en">
<head>
<meta charset="utf-8">
<title>Keystone Flooring — Business Cards</title>
<link href="https://fonts.googleapis.com/css2?family=Jost:wght@400;500;600&family=Libre+Caslon+Text:wght@400;700&display=swap" rel="stylesheet">
<style>
  :root {
    --orange: #e8901e;
    --grey-band: #a39e9a;
    --ink: #4a4a4a;
    --rule: #c9c9c9;
    --paper: #ffffff;
    --backdrop: #e3e4e6;
  }
  * { box-sizing: border-box; margin: 0; padding: 0; }
  html, body { width: 1200px; height: 800px; overflow: hidden; }
  body {
    background: var(--backdrop);
    font-family: "Jost", sans-serif;
    color: var(--ink);
    position: relative;
  }
  .card {
    position: absolute;
    width: 520px;
    height: 297px;
    background: var(--paper);
    box-shadow: 0 6px 18px rgba(0,0,0,0.12);
    overflow: hidden;
  }
  .card--appointment { left: 50px; top: 252px; }
  .card--contact { left: 630px; top: 252px; }

  .card__bands { position: absolute; left: 0; bottom: 0; width: 520px; height: 60px; }
  .web {
    position: absolute;
    bottom: 14px;
    color: #fff;
    font-size: 15px;
    font-weight: 500;
    letter-spacing: 0.2px;
  }

  .wordmark {
    font-family: "Libre Caslon Text", serif;
    font-weight: 400;
    color: var(--orange);
    line-height: 1;
    white-space: nowrap;
  }

  /* Appointment side */
  .offer { position: absolute; left: 26px; top: 22px; font-size: 13px; line-height: 1.35; }
  .offer__heading { color: var(--orange); font-weight: 600; text-transform: uppercase; font-size: 13px; }
  .offer__list { list-style: none; margin-bottom: 6px; }
  .offer__list li::before { content: "▪ "; font-size: 10px; }
  .appointment { position: absolute; left: 26px; top: 156px; width: 470px; }
  .appointment__heading { color: var(--orange); font-weight: 600; font-size: 15px; margin-bottom: 4px; }
  .appointment__row { display: flex; align-items: flex-end; font-size: 12px; color: var(--orange); margin-bottom: 6px; }
  .appointment__fill { flex: 1; border-bottom: 1.5px dotted #8a8a8a; margin: 0 6px 3px; }
  .appointment__fill--date { flex: 1.4; }
  .card--appointment .wordmark { position: absolute; right: 26px; top: 78px; font-size: 30px; }
  .tagline { position: absolute; right: 26px; top: 116px; font-size: 14px; color: var(--ink); }

  /* Contact side */
  .person { position: absolute; left: 26px; top: 24px; }
  .person__name { font-family: "Libre Caslon Text", serif; color: var(--orange); font-size: 19px; }
  .person__title { font-size: 14px; color: var(--ink); }
  .rule { position: absolute; height: 1px; background: var(--rule); }
  .rule--top { left: 26px; top: 80px; width: 190px; }
  .rule--bottom { left: 26px; top: 196px; width: 468px; }
  .contact { position: absolute; left: 26px; top: 92px; font-size: 13.5px; line-height: 1.7; list-style: none; }
  .contact li { display: flex; align-items: center; gap: 7px; }
  .contact svg { width: 13px; height: 13px; fill: var(--orange); flex: none; }
  .card--contact .wordmark { position: absolute; right: 26px; top: 40px; font-size: 30px; }
  .address { position: absolute; right: 26px; top: 146px; text-align: right; font-size: 14px; line-height: 1.3; font-style: normal; }
</style>
</head>
<body>

<section class="card card--appointment" aria-label="Appointment card">
  <div class="offer">
    <p class="offer__heading">Products -</p>
    <ul class="offer__list">
      <li>Carpet ▪ Hardwood ▪ Laminate</li>
      <li>Luxury Vinyl ▪ Tile</li>
    </ul>
    <p class="offer__heading">Services -</p>
    <ul class="offer__list">
      <li>Flooring Installations</li>
      <li>Commercial Installations</li>
      <li>In-home Measurements</li>
    </ul>
  </div>

  <p class="wordmark">Keystone Flooring</p>
  <p class="tagline">flooring at an affordable price.</p>

  <div class="appointment">
    <p class="appointment__heading">Appointment -</p>
    <p class="appointment__row">Date:<span class="appointment__fill appointment__fill--date"></span>Time:<span class="appointment__fill"></span></p>
    <p class="appointment__row">Date:<span class="appointment__fill appointment__fill--date"></span>Time:<span class="appointment__fill"></span></p>
  </div>

  <svg class="card__bands" viewBox="0 0 520 60" aria-hidden="true">
    <polygon points="0,12 185,12 200,60 0,60" fill="var(--orange)"/>
    <polygon points="190,34 520,34 520,60 198,60" fill="var(--grey-band)"/>
  </svg>
  <p class="web" style="left:22px;">keystonefloorsoutlet.com</p>
</section>

<section class="card card--contact" aria-label="Contact card">
  <div class="person">
    <p class="person__name">Daniel Marsh</p>
    <p class="person__title">Sales + Design Manager</p>
  </div>
  <div class="rule rule--top"></div>
  <ul class="contact">
    <li>
      <svg viewBox="0 0 24 24" aria-hidden="true"><path d="M6.6 10.8a15.1 15.1 0 0 0 6.6 6.6l2.2-2.2a1 1 0 0 1 1-.25 11.4 11.4 0 0 0 3.6.57 1 1 0 0 1 1 1V20a1 1 0 0 1-1 1A17 17 0 0 1 3 4a1 1 0 0 1 1-1h3.5a1 1 0 0 1 1 1c0 1.25.2 2.45.57 3.57a1 1 0 0 1-.25 1z"/></svg>
      555-201-4830
    </li>
    <li>
      <svg viewBox="0 0 24 24" aria-hidden="true"><path d="M2 5h20v14H2zm2 2v.5l8 5 8-5V7zm0 3v7h16v-7l-8 5z"/></svg>
      dan@keystonefloorsoutlet.com
    </li>
  </ul>

  <p class="wordmark">Keystone Flooring</p>
  <address class="address">1520 Harbor View Rd.<br>Port Lanton, FL 33900</address>
  <div class="rule rule--bottom"></div>

  <svg class="card__bands" viewBox="0 0 520 60" aria-hidden="true">
    <polygon points="0,34 300,34 292,60 0,60" fill="var(--grey-band)"/>
    <polygon points="300,12 520,12 520,60 286,60" fill="var(--orange)"/>
  </svg>
  <p class="web" style="right:22px;">keystonefloorsoutlet.com</p>
</section>

</body>
</html>
```